Corvell Bookkeeping Services business cards

looking for a double sided business card design. My logo is attached. I am looking for a design similar to the attached. Keen to see what my logo in white on the blue background would look like.

```html
<!DOCTYPE html>
<html lang="en">
<head>
<meta charset="utf-8">
<title>Corvell Bookkeeping Services – Business Cards</title>
<link href="https://fonts.googleapis.com/css2?family=Poppins:wght@400;500;600;700&display=swap" rel="stylesheet">
<style>
  :root {
    --navy: #1f3a6e;
    --green: #8cc63f;
    --white: #ffffff;
    --ink: #1b1b1b;
    --backdrop: #242424;
  }
  * { box-sizing: border-box; margin: 0; padding: 0; }
  html, body { width: 1200px; height: 711px; overflow: hidden; }
  body {
    background: var(--backdrop);
    font-family: "Poppins", sans-serif;
    position: relative;
  }
  .card {
    position: absolute;
    top: 196px;
    width: 520px;
    height: 318px;
    border-radius: 18px;
    overflow: hidden;
    box-shadow: 0 10px 28px rgba(0,0,0,.55);
  }
  .card-front { left: 45px; background: var(--navy); }
  .card-back { left: 635px; background: var(--white); }

  .wordmark {
    position: absolute;
    display: flex;
    align-items: center;
    gap: 12px;
    font-weight: 700;
    line-height: 1.05;
  }
  .wordmark-square {
    width: 34px; height: 34px;
    border-radius: 4px;
    flex: none;
  }
  .card-front .wordmark {
    left: 0; right: 0; top: 0; bottom: 0;
    justify-content: center;
    color: var(--white);
    font-size: 30px;
  }
  .card-front .wordmark-square { background: var(--white); width: 44px; height: 44px; }
  .wordmark small { display: block; font-size: 14px; letter-spacing: 1.5px; text-transform: uppercase; }

  .band { position: absolute; inset: 0; }

  .card-back .wordmark {
    left: 34px; top: 96px;
    color: var(--navy);
    font-size: 22px;
  }
  .card-back .wordmark-square { background: var(--navy); }
  .card-back .wordmark small { font-size: 10.5px; letter-spacing: 1.1px; }

  .person {
    position: absolute;
    right: 28px; top: 26px;
    text-align: right;
  }
  .person-name { font-size: 22px; font-weight: 500; line-height: 1.1; }
  .person-name .first { color: var(--green); }
  .person-name .last { color: var(--navy); }
  .person-role { font-size: 12.5px; color: var(--ink); margin-top: 2px; }
  .accent-tab {
    position: absolute;
    right: 0; top: 22px;
    width: 12px; height: 40px;
    background: var(--green);
  }

  .address {
    position: absolute;
    left: 34px; top: 166px;
    font-size: 12px;
    line-height: 1.4;
    color: var(--ink);
  }
  .contacts {
    position: absolute;
    left: 34px; bottom: 16px;
    list-style: none;
    color: var(--white);
    font-size: 12px;
    line-height: 1.65;
  }
  .contacts li { display: flex; align-items: center; gap: 9px; }
  .contacts svg { width: 12px; height: 12px; flex: none; }
</style>
</head>
<body>

<section class="card card-front" aria-label="Card front">
  <div class="wordmark">
    <span class="wordmark-square"></span>
    <span>Corvell<small>Bookkeeping Services</small></span>
  </div>
</section>

<section class="card card-back" aria-label="Card back">
  <svg class="band" viewBox="0 0 520 318" preserveAspectRatio="none" aria-hidden="true">
    <polygon points="0,238 520,146 520,318 0,318" fill="#1f3a6e"/>
  </svg>

  <div class="accent-tab"></div>
  <div class="person">
    <p class="person-name"><span class="first">Daniel</span> <span class="last">Hartley</span></p>
    <p class="person-role">Bookkeeper / BAS Agent</p>
  </div>

  <div class="wordmark">
    <span class="wordmark-square"></span>
    <span>Corvell<small>Bookkeeping Services</small></span>
  </div>

  <p class="address">PO Box 4721<br>Yarrowdale, QLD 4412</p>

  <ul class="contacts">
    <li>
      <svg viewBox="0 0 12 12"><rect x="3" y="1" width="6" height="10" rx="1.2" fill="none" stroke="#8cc63f" stroke-width="1.3"/><circle cx="6" cy="9" r=".7" fill="#8cc63f"/></svg>
      0491 555 218
    </li>
    <li>
      <svg viewBox="0 0 12 12"><rect x="1" y="2.5" width="10" height="7" rx="1" fill="none" stroke="#8cc63f" stroke-width="1.3"/><path d="M1.5 3l4.5 3.5L10.5 3" fill="none" stroke="#8cc63f" stroke-width="1.2"/></svg>
      hello@corvellbookkeeping.com.au
    </li>
    <li>
      <svg viewBox="0 0 12 12"><circle cx="6" cy="6" r="4.8" fill="none" stroke="#8cc63f" stroke-width="1.2"/><ellipse cx="6" cy="6" rx="2" ry="4.8" fill="none" stroke="#8cc63f" stroke-width="1"/><path d="M1.2 6h9.6" stroke="#8cc63f" stroke-width="1"/></svg>
      www.corvellbookkeeping.com.au
    </li>
  </ul>
</section>

</body>
</html>
```